Brightwave Audiology Letterhead redesign project

We need a full redesign of our current letterhead to make it consistent with the look and feel of our website design www.brightwaveaudio.com.au. It will need to include all information on the current version attached. The letterhead is used for sending medical reports and general correspondence. It should make use of our corporate colours (purple and teal) as per the logo on the existing file. The letterhead should be bold and eye-catching.

Target Market(s)

Medical practitioners.

Font styles to use
Sans Serif

Requirements
Must have
• It will need to include all information on the current version. Must have a premium, professional, high-end look and feel.
Nice to have
• Bold and eye-catching letterhead that reinforces the Brightwave Audiology brand. To stand out from other traditional letterheads.
Should not have
• The design should not be too cluttered or 'busy'

```html
<!DOCTYPE html>
<html lang="en">
<head>
<meta charset="utf-8">
<title>Brightwave Audiology Letterhead</title>
<link rel="stylesheet" href="https://fonts.googleapis.com/css2?family=Nunito:wght@800&family=Open+Sans:wght@400&family=Lato:wght@700&family=Tinos:wght@400;700&display=swap">
<style>
  :root {
    --purple: #6b2c91;
    --teal: #0aad86;
    --paper: #f9f9f9;
    --backdrop: #6e6e6e;
    --ink: #2a2a2a;
    --contact-ink: #3a3a3a;
  }
  html, body { margin: 0; padding: 0; width: 1200px; height: 1200px; overflow: hidden; background: var(--backdrop); }
  .letterhead {
    position: absolute; left: 220px; top: 30px;
    width: 761px; height: 1140px;
    background: var(--paper);
    overflow: hidden;
  }
  .brand { position: absolute; left: 55px; top: 38px; }
  .brand-name {
    display: flex; align-items: center; gap: 10px;
    font-family: "Nunito", sans-serif; font-weight: 800;
    font-size: 44px; line-height: 1; color: var(--purple); letter-spacing: -0.5px;
  }
  .brand-dot { width: 14px; height: 14px; border-radius: 50%; background: var(--teal); }
  .brand-tagline {
    margin-top: 6px;
    font-family: "Nunito", sans-serif; font-weight: 800;
    font-size: 13px; color: var(--teal);
  }
  .contact-tab {
    position: absolute; left: 656px; top: 0; width: 48px; height: 142px;
    background: var(--purple); border-radius: 0 0 5px 5px;
  }
  .contact-icon { position: absolute; left: 13px; width: 22px; height: 22px; }
  .contact-list {
    position: absolute; right: 113px; top: 45px; margin: 0; padding: 0; list-style: none;
    text-align: right; font-family: "Open Sans", sans-serif; font-size: 16px;
    line-height: 22px; color: var(--contact-ink);
  }
  .letter-body {
    position: absolute; left: 69px; top: 232px; width: 630px;
    font-family: "Tinos", serif; font-size: 15px; line-height: 18px; color: var(--ink);
  }
  .letter-body p { margin: 0; }
  .date { margin-bottom: 56px !important; }
  .recipient { margin-bottom: 56px !important; }
  .subject { font-weight: 700; margin-bottom: 56px !important; }
  .greeting, .para { margin-bottom: 18px !important; }
  .justify { text-align: justify; }
  .signoff { margin-top: 56px !important; }
  .website {
    position: absolute; left: 0; right: 0; top: 1018px; text-align: center;
    font-family: "Lato", sans-serif; font-weight: 700; font-size: 16px;
    letter-spacing: 1.2px; color: var(--purple);
  }
  .address-band {
    position: absolute; left: 0; right: 0; bottom: 0; height: 80px;
    background: var(--teal); display: flex; align-items: center; justify-content: center;
    font-family: "Lato", sans-serif; font-weight: 700; font-size: 17px; color: #fff;
  }
</style>
</head>
<body>
<main class="letterhead">
  <header>
    <div class="brand">
      <div class="brand-name">Brightwave Audiology <span class="brand-dot"></span></div>
      <div class="brand-tagline">independent hearing solutions specialist</div>
    </div>

    <ul class="contact-list">
      <li>07 5550 1234</li>
      <li>07 5550 5678</li>
      <li>hello@brightwaveaudio.com.au</li>
    </ul>

    <div class="contact-tab">
      <svg class="contact-icon" style="top:46px" viewBox="0 0 22 22" aria-label="Phone">
        <circle cx="11" cy="11" r="11" fill="#fff"/>
        <path d="M7.5 6.5c.6-.6 1.3-.5 1.6.1l.8 1.6c.2.5 0 .9-.4 1.2l-.5.4c.5 1.2 1.4 2.1 2.6 2.6l.4-.5c.3-.4.8-.5 1.2-.3l1.6.8c.6.3.7 1 .1 1.6l-.7.7c-.8.8-3.3.2-5.4-1.9S6 8 6.8 7.2z" fill="var(--teal)"/>
      </svg>
      <svg class="contact-icon" style="top:70px" viewBox="0 0 22 22" aria-label="Fax">
        <circle cx="11" cy="11" r="11" fill="#fff"/>
        <rect x="8" y="5.5" width="6" height="3.5" fill="var(--teal)"/>
        <rect x="6" y="9" width="10" height="5" rx="1" fill="var(--teal)"/>
        <rect x="8" y="12.5" width="6" height="4" fill="var(--teal)" stroke="#fff" stroke-width="0.8"/>
      </svg>
      <svg class="contact-icon" style="top:94px" viewBox="0 0 22 22" aria-label="Email">
        <circle cx="11" cy="11" r="11" fill="#fff"/>
        <rect x="6" y="7.5" width="10" height="7" rx="1" fill="var(--teal)"/>
        <path d="M6.5 8l4.5 3.5L15.5 8" fill="none" stroke="#fff" stroke-width="0.9"/>
      </svg>
    </div>
  </header>

  <section class="letter-body">
    <p class="date">Issuing date: May 5, 2012</p>
    <p class="recipient">Name of employee: Mr. xyz<br>Address of employee<br>address line 2</p>
    <p class="subject">Ref: Promotion as an Assistant secretary</p>
    <p class="greeting">Dear Mr. xyz,</p>
    <p class="para">I have the pleasure to inform you that you have been promoted as Assistant secretary in the<br>department of the company. You are required to take charge of the new post from 15th May,<br>2012. Please accept my hearty congratulations on your promotion.</p>
    <p class="para justify">Your salary scale in the promoted cadre will be Tk. 16,000 and from 15th May, your basic salary will be fixed at Tk. 12,000 in the said scale. You will be entitled to all other allowances as applicable to the staff-II of the company. Other services conditions remain unchanged.</p>
    <p class="para">Please acknowledge receipt of this letter.</p>
    <p class="signoff">Yours sincerely,</p>
  </section>

  <footer>
    <div class="website">www.brightwaveaudio.com.au</div>
    <div class="address-band">CLINIC 48 Harlow Street, Ashford, Qld 4350</div>
  </footer>
</main>
</body>
</html>
```